Newspaper Ad for a new concept medical clinic

I have uploaded a sample ad. I would prefer the black areas to be the same color blue as the word CarePeak in the attached file. Instead of a doctor I would like a concerned or worried looking middle age couple 40s/50s as a picture.

702 number will need to change to a toll free number that I will have available next week.
Change web address to www.varbelmd-example.com

I would like the bullet points to be changed as follows:
- Affordable Access To Board Certified Physician
- Committment To Excellence In Primary Medical Care
- $10 Office Visits / No Charge Telemedicine Visits
- Adults - $69/month & Teens to Age 26 - $19/month
- Lowest Rates For Lab Tests, Imaging, and Medications

Keep the As Seen In section unchanged
Updates

Ii would like full color. Also I will call the local newspaper today and find the exact dimensenions and update everyone. Thank you all for interest and input.

3 columns(4.9" wide) by 5.25" tall

Please review your submission for readability at the size proposed. The actual ad size is 4.9" wide by 5.25 in tall. There are many wonderful submissions. I am truly impressed.

Full Color

Make sure the copy is readable at this ad size. My last request is for you to add the following term somewhere: Limited Enrollment Call Now

Industry/Entity Type

Medical

```html
<!DOCTYPE html>
<html lang="en">
<head>
<meta charset="utf-8">
<title>CarePeak Direct Primary Care – Newspaper Ad</title>
<link rel="stylesheet" href="https://fonts.googleapis.com/css2?family=Montserrat:wght@300;400;600;700&display=swap">
<style>
  :root {
    --blue-deep: #0f4f93;
    --blue-mid: #1a72bd;
    --blue-light: #2b8fd6;
    --brand-blue: #1f7cc4;
    --orange: #f39325;
    --orange-light: #f7a544;
    --white: #ffffff;
    --page: #ffffff;
    --photo-dark: #8a8a8e;
    --photo-mid: #c9b7a8;
    --photo-warm: #b9a9a0;
    --photo-light: #e9e6ea;
  }
  * { margin: 0; padding: 0; box-sizing: border-box; }
  html, body { width: 935px; height: 1200px; overflow: hidden; }
  body {
    font-family: "Montserrat", Arial, sans-serif;
    background: var(--page);
    display: flex;
    align-items: center;
    justify-content: center;
  }

  /* 4.9in x 5.25in ad */
  .ad {
    position: relative;
    width: 935px;
    height: 1002px;
    overflow: hidden;
    background: linear-gradient(180deg, var(--blue-deep) 0%, var(--blue-mid) 45%, var(--blue-light) 68%, var(--blue-mid) 100%);
  }

  .headline {
    position: absolute;
    top: 34px; left: 0; width: 100%;
    text-align: center;
    color: var(--white);
    font-weight: 300;
    font-size: 56px;
    line-height: 1.1;
    text-shadow: 0 2px 4px rgba(0,0,0,0.25);
  }
  .headline strong { font-weight: 700; }

  .photo-band {
    position: absolute;
    top: 0; left: 0;
    width: 935px; height: 1002px;
  }

  .enrollment {
    position: absolute;
    top: 614px; left: 0; width: 100%;
    text-align: center;
    color: var(--orange-light);
    font-weight: 700;
    font-size: 27px;
    letter-spacing: 1px;
    text-transform: uppercase;
  }

  .benefits {
    position: absolute;
    top: 658px; left: 0; width: 100%;
    list-style: none;
    text-align: center;
    color: var(--white);
    font-weight: 400;
    font-size: 23px;
    line-height: 30px;
    letter-spacing: 0.3px;
  }

  .brand-card {
    position: absolute;
    left: 220px; top: 820px;
    width: 518px; height: 132px;
    background: var(--white);
    border-radius: 24px 24px 0 0;
    box-shadow: 0 -2px 10px rgba(0,0,0,0.15);
    text-align: center;
    padding-top: 18px;
  }
  .brand-name {
    display: inline-flex;
    align-items: center;
    gap: 12px;
    color: var(--brand-blue);
    font-weight: 400;
    font-size: 56px;
    line-height: 1;
  }
  .brand-mark {
    width: 26px; height: 26px;
    border-radius: 50%;
    background: var(--orange);
  }
  .brand-tagline {
    margin-top: 8px;
    color: var(--orange);
    font-weight: 600;
    font-size: 24px;
  }

  .contact-bar {
    position: absolute;
    left: 0; bottom: 0;
    width: 100%; height: 50px;
    background: var(--orange);
    display: flex;
    align-items: center;
    justify-content: space-between;
    padding: 0 36px;
    color: var(--white);
  }
  .contact-call { font-size: 21px; font-weight: 400; }
  .contact-call strong { font-weight: 700; }
  .contact-web { font-size: 26px; font-weight: 700; }
</style>
</head>
<body>
  <main class="ad">
    <h1 class="headline">Can’t Afford <strong>Health</strong> Benefits?</h1>

    <svg class="photo-band" viewBox="0 0 935 1002" width="935" height="1002">
      <defs>
        <linearGradient id="photoTone" x1="0" y1="0" x2="1" y2="0">
          <stop offset="0" style="stop-color: var(--photo-dark)"/>
          <stop offset="0.35" style="stop-color: var(--photo-mid)"/>
          <stop offset="0.6" style="stop-color: var(--photo-warm)"/>
          <stop offset="1" style="stop-color: var(--photo-light)"/>
        </linearGradient>
        <linearGradient id="edgeTone" x1="0" y1="0" x2="1" y2="0">
          <stop offset="0" style="stop-color: var(--orange-light); stop-opacity: 0.35"/>
          <stop offset="0.5" style="stop-color: var(--orange)"/>
          <stop offset="1" style="stop-color: var(--orange-light); stop-opacity: 0.45"/>
        </linearGradient>
      </defs>
      <path role="img" aria-label="Photo of a worried middle-aged couple looking into the distance"
            d="M0 178 Q 360 118 935 150 L 935 600 Q 470 566 0 600 Z"
            fill="url(#photoTone)"/>
      <path d="M0 178 Q 360 118 935 150" fill="none" stroke="url(#edgeTone)" stroke-width="6"/>
      <path d="M0 600 Q 470 566 935 600" fill="none" stroke="url(#edgeTone)" stroke-width="6"/>
    </svg>

    <p class="enrollment">Limited Enrollment – Call Now</p>

    <ul class="benefits">
      <li>- Affordable Access To Board Certified Physician</li>
      <li>- Committment To Excellence In Primary Medical Care</li>
      <li>- $10 Office Visits / No Charge Telemedicine Visits</li>
      <li>- Adults - $69/month &amp; Teens to Age 26 - $19/month</li>
      <li>- Lowest Rates For Lab Tests, Imaging, and Medications</li>
    </ul>

    <div class="brand-card">
      <div class="brand-name">CarePeak<span class="brand-mark"></span></div>
      <div class="brand-tagline">Direct Primary Care</div>
    </div>

    <footer class="contact-bar">
      <span class="contact-call"><strong>Call to sign up</strong>: 702-555-0148</span>
      <span class="contact-web">www.varbelmd-example.com</span>
    </footer>
  </main>
</body>
</html>
```